Business Card Design

Quorvel Software Limited develops and sells venue and event management software called Quorvel Stagehand, which is available in the cloud or on-premise. The company was established in 1986. Most of our customers are performing arts venues, museums and festivals. Our existing design is a bit dull. We need to convey that we are both innovative and reliable.
Not all our people show their mobile phone numbers on their cards, so the design needs to work land line and mobile or land line only.

Industry/Entity Type

Software

Contact Information for Business Card

Helen Brackwood
Director
Quorvel Software Limited
42B Millbank Lane, Epsom, Surrey, KT19 3DW
Telephone: +44 (0)1372 904213
Mobile: +44 (0)7700 900562
Email: hbrackwood@quorvel.example
Web: www.quorvel.example

```html
<!DOCTYPE html>
<html lang="en">
<head>
<meta charset="utf-8">
<title>Quorvel Software Limited – Business Card</title>
<link rel="stylesheet" href="https://fonts.googleapis.com/css2?family=Open+Sans:wght@400;600;700&display=swap">
<style>
  :root {
    --bg: #e9e6e1;
    --white: #ffffff;
    --paper-grey: #e4e6e8;
    --blue-light: #2aa2d6;
    --blue-mid: #1e86bf;
    --blue-deep: #0f5a8c;
    --blue-ink: #1d5f8c;
    --blue-name: #2a8cc4;
    --text-grey: #5b6670;
    --back-top: #1b6fa6;
    --back-bottom: #0d4c7a;
  }
  html, body {
    margin: 0;
    width: 1200px;
    height: 1023px;
    overflow: hidden;
    background: var(--bg);
    font-family: "Open Sans", Arial, sans-serif;
  }
  .canvas { position: relative; width: 1200px; height: 1023px; }
  .card {
    position: absolute;
    width: 600px;
    height: 343px;
    border-radius: 4px;
    overflow: hidden;
    box-shadow: 0 10px 28px rgba(0,0,0,.18);
  }
  .card-front { left: 80px; top: 150px; background: var(--white); }
  .card-back {
    left: 520px; top: 540px;
    background: linear-gradient(160deg, var(--back-top), var(--back-bottom));
  }
  .front-shapes { position: absolute; inset: 0; }

  .wordmark {
    position: absolute;
    left: 26px; top: 96px;
    margin: 0;
    font-size: 48px;
    font-weight: 700;
    letter-spacing: 2px;
    color: var(--blue-ink);
    line-height: 1;
  }
  .person { position: absolute; left: 60px; top: 150px; width: 220px; text-align: right; }
  .person-name { margin: 0; font-size: 18px; font-weight: 600; color: var(--blue-name); letter-spacing: .5px; line-height: 22px; }
  .person-role { margin: 1px 0 0; font-size: 10px; color: var(--text-grey); letter-spacing: 1px; }

  .contacts {
    position: absolute; left: 330px; top: 172px;
    list-style: none; margin: 0; padding: 0;
    color: var(--white); font-size: 13px; line-height: 24px;
  }
  .contacts li { display: flex; align-items: center; gap: 8px; }
  .icon { width: 14px; height: 14px; flex: none; }

  .company {
    position: absolute; left: 450px; top: 26px;
    color: var(--white); font-size: 11.5px; line-height: 19px;
  }
  .company-name { margin: 0; font-weight: 700; }
  .company p { margin: 0; }
  .company .tel { display: flex; align-items: center; gap: 6px; }

  .back-mark {
    position: absolute; left: 0; right: 0; top: 145px;
    display: flex; justify-content: center; align-items: center; gap: 12px;
    color: var(--white); font-size: 40px; font-weight: 700; letter-spacing: 3px;
  }
  .back-mark .dot { width: 16px; height: 16px; background: var(--white); }
</style>
</head>
<body>
<div class="canvas">

  <section class="card card-front">
    <svg class="front-shapes" width="600" height="343" viewBox="0 0 600 343">
      <rect width="600" height="343" fill="var(--white)"/>
      <polygon points="0,0 360,0 335,82 0,82" fill="var(--paper-grey)"/>
      <polygon points="360,0 600,0 600,150 303,150" fill="var(--blue-light)"/>
      <polygon points="360,0 470,150 303,150" fill="var(--blue-mid)"/>
      <polygon points="303,150 600,150 600,343 230,343" fill="var(--blue-deep)"/>
      <polygon points="230,343 380,300 430,343" fill="var(--white)"/>
    </svg>

    <h1 class="wordmark">QUORVEL</h1>

    <div class="person">
      <p class="person-name">HELEN BRACKWOOD</p>
      <p class="person-role">DIRECTOR</p>
    </div>

    <ul class="contacts">
      <li>
        <svg class="icon" viewBox="0 0 14 14"><rect x="1" y="1" width="12" height="12" rx="2" fill="none" stroke="#fff" stroke-width="1.3"/><rect x="5" y="3.5" width="4" height="7" rx="0.8" fill="#fff"/></svg>
        +44 (0)7700 900562
      </li>
      <li>
        <svg class="icon" viewBox="0 0 14 14"><rect x="1" y="1" width="12" height="12" rx="2" fill="none" stroke="#fff" stroke-width="1.3"/><path d="M3.5 5l3.5 2.5 3.5-2.5M3.5 4.5h7v5h-7z" fill="none" stroke="#fff" stroke-width="1"/></svg>
        hbrackwood@quorvel.example
      </li>
      <li>
        <svg class="icon" viewBox="0 0 14 14"><rect x="1" y="1" width="12" height="12" rx="2" fill="none" stroke="#fff" stroke-width="1.3"/><circle cx="7" cy="7" r="3.5" fill="none" stroke="#fff" stroke-width="1"/><path d="M3.5 7h7M7 3.5v7" stroke="#fff" stroke-width="0.8"/></svg>
        www.quorvel.example
      </li>
    </ul>

    <div class="company">
      <p class="company-name">Quorvel Software Limited</p>
      <p>42B Millbank Lane, Epsom</p>
      <p>Surrey, KT19 3DW</p>
      <p class="tel">
        <svg class="icon" viewBox="0 0 14 14"><rect x="1" y="1" width="12" height="12" rx="2" fill="#fff"/><path d="M4.5 3.5l1.5 0 .7 2-1 .8a5 5 0 0 0 2 2l.8-1 2 .7v1.5c-3.5.5-6.5-2.5-6-6z" fill="var(--blue-mid)"/></svg>
        +44 (0)1372 904213
      </p>
    </div>
  </section>

  <section class="card card-back">
    <div class="back-mark"><span class="dot"></span>QUORVEL</div>
  </section>

</div>
</body>
</html>
```